Velmora, Inc. Website

Looking for a website design and build for Velmora, Inc. an intellectual property incubator for the recreational and medical cannabis space in California. Our logo and brand identity has been completed website so w can begin our SEO leg of brand development.

See more details in Must haves and Nice to Haves

Target Market(s)

Target market

Vision

Our proprietary ideas have been developed to shift the approach on how whole body wellness and healing is achieved. Velmora's patent pending designs and formulations are rooted in the desire to find the most efficient, customizable, and convenient  method to precisely micro-despense whole plant cannabis extracts. 

Our ideas, designs and development team are supported by leading chemists specializing in cannabis extraction technology, leading medical doctors collaborating to develop our proprietary cannabis formulations and a passion to shift landscape of healing from a dependency on isolated symptom treatment to whole body, whole plant, whole life wellness for ourselves and our families. 

Goal

Develop, patent, and trademark our proprietary devices, formulations, and ideas for the purpose of licensing, manufacturing and distributing in the Cannabis Industry.

Industry/Entity Type

Medical

Coding

Coded - Design and coding required

Number of Pages Required

5+ page

Font styles to use
Other font styles liked:
• See Brand Identity Guide

Requirements
Must have
• Look and Feel: We are developing products, intellectual property and platforms to bring together the medical, health & wellness, and cannabis industries to provide individuals and families alike a innovative solutions to chronic illness, mood disorders, and over all wellbeing.
• Page Titles
• Home - Landing Page
• Vision-
• IP Technology & Products - will remain under construction
• Team
• Strategic Partners – will remain under construction
• Invest- will need a form to aquire contact information as well as have some questions that need to be answered to help evaluate to the potential interested party
• Contact Us– Velmora address and info@ email
Nice to have
• Images - wellness, balance, health, healing, herbs, not just cannabis, aromatherapy, mediation, energy work, dna, scientific research, microdosing, medical testing
• Style sleek and innovative - cutting edge technology - inspire to learn more
• For Colors and Fonts - See Brand Identity Guide
• Site layouts that we like are:
• http://www.thepravexgroup.example
• https://www.duneloftcare.example
• https://www.sorvanti.example
• https://www.quolt.example
• https://www.tarefy.example
Should not have
• Should not have to many cannabis images - imagery should balanced between cannabis, medical & recreational, health and wellness, mental health

```html
<!DOCTYPE html>
<html lang="en">
<head>
<meta charset="utf-8">
<title>Velmora, Inc. — We are your voice for medical cannabis</title>
<link rel="stylesheet" href="https://fonts.googleapis.com/css2?family=Poppins:wght@300;400;500&family=Lato:wght@300&family=Merriweather:ital,wght@1,300&display=swap">
<style>
  :root {
    --overlay: rgba(92, 52, 120, 0.38);
    --leaf-deep: #2f4a2a;
    --leaf-mid: #5f7d3a;
    --leaf-light: #a7b85a;
    --skin-glow: #c9a3b8;
    --white: #ffffff;
    --nav-green: #5fd13a;
    --brand-purple: #7a3fb0;
  }
  * { margin: 0; padding: 0; box-sizing: border-box; }
  html, body { width: 1200px; height: 605px; overflow: hidden; }
  body { font-family: "Poppins", sans-serif; background: #3a2f44; }

  .hero { position: relative; width: 1200px; height: 605px; overflow: hidden; }

  .hero-photo {
    position: absolute; inset: 0;
    background:
      radial-gradient(ellipse 260px 340px at 820px 360px, var(--skin-glow) 0%, rgba(201,163,184,0) 75%),
      radial-gradient(ellipse 200px 160px at 430px 120px, var(--leaf-light) 0%, rgba(167,184,90,0) 80%),
      radial-gradient(ellipse 300px 200px at 360px 520px, #9c8aa6 0%, rgba(156,138,166,0) 80%),
      linear-gradient(90deg, var(--leaf-deep) 0%, var(--leaf-mid) 35%, #6d7f45 60%, var(--leaf-deep) 100%);
  }
  .hero-overlay { position: absolute; inset: 0; background: var(--overlay); }

  .site-header {
    position: absolute; top: 0; left: 0; right: 0; height: 64px;
  }
  .brand {
    position: absolute; left: 51px; top: 6px;
    display: flex; align-items: center; gap: 10px;
  }
  .brand-mark {
    width: 52px; height: 52px; border-radius: 50%;
    border: 1.5px solid var(--white);
  }
  .brand-name {
    font-family: "Lato", sans-serif; font-weight: 300;
    font-size: 24px; color: var(--white); letter-spacing: 0.2px;
  }
  .main-nav { position: absolute; top: 24px; left: 0; right: 0; }
  .main-nav a {
    position: absolute; font-size: 9.5px; color: var(--nav-green);
    text-decoration: none; white-space: nowrap;
  }

  .hero-copy { position: absolute; left: 110px; top: 226px; }
  .hero-title {
    font-weight: 300; font-size: 40px; line-height: 1.1;
    color: var(--white); letter-spacing: 0.3px;
  }
  .hero-subtitle {
    font-family: "Merriweather", serif; font-style: italic; font-weight: 300;
    font-size: 27px; color: var(--white); margin-top: 4px;
  }
  .hero-actions { display: flex; gap: 16px; margin-top: 17px; margin-left: 5px; }
  .btn {
    display: inline-flex; align-items: center; justify-content: center;
    height: 31px; font-size: 9.5px; font-weight: 500;
    color: var(--white); text-decoration: none;
  }
  .btn-primary { width: 114px; background: var(--brand-purple); }
  .btn-outline { width: 150px; border: 1.5px solid var(--white); }

  .slider-arrow {
    position: absolute; top: 290px; width: 44px; height: 44px;
  }
  .slider-arrow.prev { left: 25px; }
  .slider-arrow.next { left: 1130px; }
</style>
</head>
<body>
  <section class="hero">
    <div class="hero-photo" role="img" aria-label="Smiling woman jogging along a sunlit forest path, wearing earphones, under a purple tint"></div>
    <div class="hero-overlay"></div>

    <header class="site-header">
      <div class="brand">
        <span class="brand-mark"></span>
        <span class="brand-name">Velmora, Inc</span>
      </div>
      <nav class="main-nav">
        <a href="#" style="left:640px">Vision</a>
        <a href="#" style="left:692px">IP Technology &amp; Products</a>
        <a href="#" style="left:828px">Invest</a>
        <a href="#" style="left:880px">Strategic Partners</a>
        <a href="#" style="left:985px">Team</a>
        <a href="#" style="left:1037px">News</a>
        <a href="#" style="left:1087px">Contact Us</a>
      </nav>
    </header>

    <div class="hero-copy">
      <h1 class="hero-title">We are your voice</h1>
      <p class="hero-subtitle">for medical cannabis</p>
      <div class="hero-actions">
        <a href="#" class="btn btn-primary">Our Vision</a>
        <a href="#" class="btn btn-outline">Join the program</a>
      </div>
    </div>

    <svg class="slider-arrow prev" viewBox="0 0 44 44" aria-label="Previous slide">
      <circle cx="22" cy="22" r="21" fill="none" stroke="#fff" stroke-width="1"/>
      <path d="M30 22H14M20 16l-6 6 6 6" fill="none" stroke="#fff" stroke-width="1.2"/>
    </svg>
    <svg class="slider-arrow next" viewBox="0 0 44 44" aria-label="Next slide">
      <circle cx="22" cy="22" r="21" fill="none" stroke="#fff" stroke-width="1"/>
      <path d="M14 22h16M24 16l6 6-6 6" fill="none" stroke="#fff" stroke-width="1.2"/>
    </svg>
  </section>
</body>
</html>
```